Motorcycle Shop Business Card

New business card for Motorcycle repair and customization shop.Business name: Copper Falcon Chris Morris443-865-5190, 7214 Quarry Lane Halvern, MD 21098. www.dale@copperfalconcustoms.example. I uploaded some motorcycle images and logo and a couple of our calendar shoots. They do not have to be used on card just examples of some of our work and past graphic work.
We work on Vantor Brennick and Custom Built Motorcycles.

Looking for front and back design

Target Market(s)

Motorcycle owners

Industry/Entity Type

Motorcycle Part

```html
<!DOCTYPE html>
<html lang="en">
<head>
<meta charset="utf-8">
<title>Copper Falcon Business Card</title>
<link href="https://fonts.googleapis.com/css2?family=Montserrat:wght@400;500;600;700&display=swap" rel="stylesheet">
<style>
  :root {
    --stage-top: #c6c5ce;
    --stage-bottom: #5c5b61;
    --card-dark: #201d1e;
    --card-light: #dde0f4;
    --wordmark-light: #c9cbe0;
    --accent-red: #8b3535;
    --ink: #1e1b1c;
  }
  * { margin: 0; padding: 0; box-sizing: border-box; }
  html, body { width: 1200px; height: 1200px; overflow: hidden; }
  body {
    position: relative;
    background: linear-gradient(to bottom, var(--stage-top), var(--stage-bottom));
    font-family: "Montserrat", sans-serif;
  }
  .card {
    position: absolute;
    left: 267px;
    width: 708px;
    height: 404px;
  }
  .card-front { top: 132px; background: var(--card-light); }
  .card-back { top: 667px; background: var(--card-dark); }
  .card-face {
    position: absolute;
    inset: 22px 22px 22px 23px;
    display: flex;
    flex-direction: column;
    align-items: center;
    text-align: center;
  }
  .card-front .card-face {
    background: var(--card-dark);
    box-shadow: inset 0 0 6px rgba(0,0,0,0.6);
  }
  .card-back .card-face {
    background: var(--card-light);
    box-shadow: inset 0 0 8px rgba(0,0,0,0.35);
  }
  .wordmark-front {
    color: var(--wordmark-light);
    font-weight: 600;
    font-size: 46px;
    letter-spacing: 1px;
    line-height: 1;
    margin-top: 146px;
  }
  .tagline {
    color: var(--accent-red);
    font-weight: 500;
    font-size: 14px;
    line-height: 17px;
    margin-top: 44px;
  }
  .owner-name {
    color: var(--ink);
    font-weight: 600;
    font-size: 53px;
    letter-spacing: 1px;
    margin-top: 28px;
    line-height: 1;
  }
  .owner-role {
    color: var(--ink);
    font-weight: 500;
    font-size: 19px;
    margin-top: 12px;
  }
  .wordmark-back {
    color: var(--accent-red);
    font-weight: 600;
    font-size: 30px;
    letter-spacing: 1px;
    margin-top: 46px;
  }
  .contact {
    color: var(--ink);
    font-weight: 500;
    font-size: 20px;
    line-height: 30px;
    margin-top: 52px;
  }
</style>
</head>
<body>
  <section class="card card-front">
    <div class="card-face">
      <div class="wordmark-front">COPPER FALCON</div>
      <p class="tagline">motorcycle<br>repair &amp; customization</p>
    </div>
  </section>

  <section class="card card-back">
    <div class="card-face">
      <h1 class="owner-name">DALE FENWICK</h1>
      <p class="owner-role">OWNER</p>
      <div class="wordmark-back">COPPER FALCON</div>
      <p class="contact">410-555-0137<br>7214 Quarry Lane Halvern, MD 21098</p>
    </div>
  </section>
</body>
</html>
```